Clear Current Monthly Bulletin

I would like to have some backgrounds designed for July - December. We would pay for each page seperately. Each month should be its own design so that we may pick the best month for each. You are welcome to submit as many designs as you like for months. Months with themes will rate higher, for example July can incorporate Independence Day, December Christmas Season/Yule/Hannukah/Holidays,October Halloween, November Thanksgiving, September Labor Day, August can be summer themed. I am attaching our newsletter that I would like the design to work around. This verbiage does not need to be on the page right now. We would like to have the verbiage for each month applied to that month on purchase. www.tolvanwiring.com is our website. We love designs that stay with our colors and website theme.

Target Market(s)

Homeowners

Industry/Entity Type

Electrical Contractor

Requirements
Must have
• Monthly or Seasonal Themes

```html
<!DOCTYPE html>
<html lang="en">
<head>
<meta charset="utf-8">
<title>Halloween 2024 – International News</title>
<link rel="stylesheet" href="https://fonts.googleapis.com/css2?family=Archivo+Black&family=Barlow+Semi+Condensed:wght@400;500&family=Oswald:wght@300;500;700&family=Playfair+Display:ital@1&display=swap">
<style>
  :root {
    --backdrop: #dcdcdc;
    --paper: #efefed;
    --ink: #1c1c1c;
    --accent-yellow: #e2d12a;
    --accent-red: #b4222f;
    --photo-night-top: #5a1f35;
    --photo-night-mid: #b23a3a;
    --photo-night-low: #3b4a78;
    --photo-day-sky: #7fb0de;
    --photo-day-pumpkin: #e07a22;
    --photo-day-ground: #8a6a4a;
    --pumpkin: #e58a2a;
  }
  * { margin: 0; padding: 0; box-sizing: border-box; }
  html, body { width: 1200px; height: 800px; overflow: hidden; }
  body { background: var(--backdrop); position: relative; color: var(--ink); }

  .page {
    position: absolute; left: 336px; top: 10px;
    width: 527px; height: 780px;
    background: var(--paper);
    box-shadow: 0 2px 10px rgba(0,0,0,.12);
  }
  .page > * { position: absolute; }

  .issue-line { left: 22px; top: 30px; font: 500 12px "Oswald", sans-serif; letter-spacing: .1px; }

  .section-band {
    left: 24px; top: 48px; width: 482px; height: 36px;
    background: var(--accent-yellow);
    display: flex; align-items: center; justify-content: space-between;
    padding: 0 10px;
  }
  .section-title { font: 700 22px "Oswald", sans-serif; letter-spacing: -.3px; }
  .section-title .highlight { color: var(--accent-red); }
  .page-number {
    background: var(--accent-red); color: #fff;
    font: 500 14px "Oswald", sans-serif;
    width: 15px; height: 18px; display: flex; align-items: center; justify-content: center;
  }

  .headline { font-family: "Archivo Black", sans-serif; letter-spacing: -1px; line-height: 1; }
  .lead-kicker { left: 22px; top: 102px; font-size: 21px; }
  .lead-title { left: 22px; top: 130px; font-size: 33px; }

  .body-copy {
    font: 400 11px/15px "Barlow Semi Condensed", sans-serif;
    text-align: justify;
  }
  .lead-col-one { left: 22px; top: 168px; width: 119px; }
  .lead-col-two { left: 152px; top: 168px; width: 143px; }

  .photo { display: block; }
  .photo-haunted {
    left: 304px; top: 104px; width: 199px; height: 239px;
    background: linear-gradient(170deg, var(--photo-night-top) 0%, var(--photo-night-mid) 40%, var(--photo-night-low) 80%, #c9c9d4 100%);
  }
  .photo-pumpkins {
    left: 237px; top: 394px; width: 261px; height: 196px;
    background: linear-gradient(90deg, var(--photo-day-pumpkin) 0%, #c9782e 35%, var(--photo-day-ground) 60%, #6f8c4a 100%),
                var(--photo-day-sky);
  }

  .pull-quote {
    left: 258px; top: 350px; width: 245px;
    font: 700 31px/1 "Oswald", sans-serif; letter-spacing: -.3px;
    display: flex; align-items: center; gap: 8px; white-space: nowrap;
  }
  .pull-quote .mark { color: var(--accent-red); font-size: 30px; }

  .trends-title { left: 22px; top: 398px; font-size: 35px; letter-spacing: -2px; }
  .trends-sub { left: 22px; top: 440px; font-size: 28px; letter-spacing: -2px; }
  .trends-copy { left: 24px; top: 478px; width: 208px; }

  .fact-box {
    left: 26px; top: 603px; width: 196px; height: 127px;
    background: var(--accent-yellow);
    padding: 12px 9px 0 11px;
  }
  .fact-heading { font: 300 22px/1 "Oswald", sans-serif; color: var(--accent-red); letter-spacing: -.3px; }
  .fact-text { margin-top: 12px; font: italic 12px/14px "Playfair Display", serif; text-align: justify; width: 180px; }
  .pumpkin-art {
    left: 90px; top: 706px; width: 100px; height: 40px;
    background: var(--pumpkin); border-radius: 20px;
  }

  .diy-title { left: 236px; top: 603px; font-size: 27px; }
  .diy-copy { left: 236px; top: 640px; width: 272px; font-size: 12.5px; line-height: 17px; text-align: left; }
</style>
</head>
<body>
  <article class="page">
    <p class="issue-line">06.26.2024 / Wendesday / #123456789</p>

    <header class="section-band">
      <h1 class="section-title"><span class="highlight">INTERNATIONAL</span> NEWS</h1>
      <span class="page-number">2</span>
    </header>

    <h2 class="headline lead-kicker">Chillingly Fun:</h2>
    <h2 class="headline lead-title">Halloween 2024</h2>

    <p class="body-copy lead-col-one">As the leaves turn vibrant shades of orange and red, and a chill creeps into the air, it's clear that Halloween is just around the corner. This beloved holiday, celebrated annually on October 31st, brings out the creative, the spooky, and the fun in all of us. Here's a look at how to make the most of Halloween 2024.</p>
    <p class="body-copy lead-col-two">One of the highlights of Halloween is the haunted house experience. This year, the city's premier haunted house attraction promises more thrills and chills than ever before. With new interactive features and spine-tingling scares around every corner, it's a must-visit for those seeking a frightful night.</p>

    <div class="photo photo-haunted" role="img" aria-label="Photo of visitors screaming inside a haunted house attraction lit in red and blue"></div>

    <p class="pull-quote"><span class="mark">“</span>SO WHAT NEXT?<span class="mark">”</span></p>

    <h2 class="headline trends-title">COSTUME</h2>
    <h2 class="headline trends-sub">TRENDS 2024</h2>
    <p class="body-copy trends-copy">Halloween costumes often reflect the biggest trends in pop culture, and this year is no exception. Expect to see plenty of costumes inspired by blockbuster movies, hit TV shows, and viral internet sensations. From superheroes to reality TV stars, creativity knows no bounds.</p>

    <div class="photo photo-pumpkins" role="img" aria-label="Photo of a carved pumpkin on a wooden table at an outdoor autumn pumpkin market"></div>

    <aside class="fact-box">
      <h3 class="fact-heading">DID YOU KNOW THAT...</h3>
      <p class="fact-text">Ancient Roots: Halloween originates from the ancient Celtic festival of Samhain, celebrated over 2,000 years ago.</p>
    </aside>
    <div class="pumpkin-art" role="img" aria-label="Illustration of three jack-o'-lanterns"></div>

    <h2 class="headline diy-title">DIY Magic</h2>
    <p class="body-copy diy-copy">Handmade costumes are making a big comeback. Whether it's a quirky character from a beloved book or a unique, punny creation, DIY costumes allow for personal expression and ingenuity. Plus, they often turn heads at costume contests!</p>
  </article>
</body>
</html>
```